creative pack design with extended budget for Nobrelia coffee product

- we need a packing design for a new product of coffee for our company Mbelo Tiru located in Uganda.
- specialty Arabica coffee grown at slopes of Mountain Elgon with rich volcanic soils located in Eastern region of Uganda.
-  we have a logo already made and has registered in Uganda. our logo colors are mixture between a lot of brown color and yellow. vacuum  plastic bags.
- there is no restrictions towards your imagination .
-  all details available
- we will launch our product through phases ;
- phase 1 is  a ground coffee : ( Turkish coffee )  2 degrees of roasting which are ( medium dark , light ) of 250 grm
b) roasted beans: 2 degrees ( medium, dark) of 250 grm & 1000 grm
- we need also to highlight the eastern spirit of Turkish coffee
- we  need designs, the info and color only will be changed depending on previous classifications

Target Market(s)
Arab countries, Turkey , Uganda, Europe
Colors
Designer to choose colors to be used in the design.
Requirements
Nice to have
- about nature , Elgon mountain , farmers, freshness, distinctive product, soul of east such as decorated cup of Turkish coffee . these just an ideas but there is no restrictions on your imagination

```html
<!DOCTYPE html>
<html lang="en">
<head>
<meta charset="utf-8">
<title>Nobrelia Coffee – Pack Range</title>
<link rel="stylesheet" href="https://fonts.googleapis.com/css2?family=Cinzel:wght@700&family=Rye&family=Roboto+Slab:wght@700&family=Lora:ital@1&display=swap">
<style>
  :root {
    --page: #ffffff;
    --brand-brown: #4a2618;

    --light-top: #a8cde6;
    --light-pattern: #c3ddef;
    --light-bottom: #eef3f6;
    --light-ink: #5f9fcc;
    --light-scene: #cfe1ee;

    --medium-top: #f0a53c;
    --medium-pattern: #f6c57a;
    --medium-bottom: #fbefd8;
    --medium-ink: #e2972c;
    --medium-scene: #f2d3a0;

    --dark-top: #e6382b;
    --dark-pattern: #f0695c;
    --dark-bottom: #3a3531;
    --dark-ink: #e23a2c;
    --dark-scene: #6a2c24;
    --dark-label: #f3ece4;
  }
  * { box-sizing: border-box; margin: 0; padding: 0; }
  html, body { width: 1200px; height: 1000px; overflow: hidden; background: var(--page); }
  .range { position: relative; width: 1200px; height: 1000px; }

  .bag {
    position: absolute;
    overflow: hidden;
    border-radius: 0.6em 0.6em 0.4em 0.4em;
    background: linear-gradient(to bottom, var(--top) 0 var(--split), var(--bottom) var(--split) 100%);
    color: var(--ink);
    text-align: center;
    box-shadow: 0 6px 14px rgba(0,0,0,0.12);
  }
  .bag > * { position: absolute; left: 0; right: 0; }

  .bag__pattern {
    top: 0; height: var(--split);
    background:
      radial-gradient(ellipse 45% 30% at 20% 25%, var(--pattern) 0%, transparent 70%),
      radial-gradient(ellipse 45% 30% at 80% 25%, var(--pattern) 0%, transparent 70%),
      radial-gradient(ellipse 50% 30% at 20% 80%, var(--pattern) 0%, transparent 70%),
      radial-gradient(ellipse 50% 30% at 80% 80%, var(--pattern) 0%, transparent 70%);
    opacity: 0.7;
  }
  .bag__seal {
    top: 0; height: 5%;
    background: linear-gradient(to bottom, rgba(0,0,0,0.08), transparent);
    border-bottom: 1px solid rgba(255,255,255,0.35);
  }
  .bag__scene {
    bottom: 0; height: var(--scene-h);
    background:
      radial-gradient(ellipse 40% 70% at 82% 100%, var(--scene) 0%, transparent 75%),
      linear-gradient(to top, var(--scene) 0%, transparent 100%);
  }

  .bag__brand { top: var(--logo-y); display: flex; flex-direction: column; align-items: center; }
  .brand__disc {
    width: 5.6em; height: 5.6em; border-radius: 50%;
    background: var(--brand-brown);
    box-shadow: 0 0 0 0.25em var(--top), 0 0 0 0.35em var(--brand-brown);
  }
  .brand__name {
    margin-top: 0.45em;
    font-family: "Cinzel", serif; font-weight: 700; font-size: 1.95em; letter-spacing: 0.03em;
    color: var(--brand-brown); line-height: 1;
  }
  .bag__tagline {
    top: var(--tag-y);
    font-family: "Lora", serif; font-style: italic; font-size: 0.45em; line-height: 1.2;
    color: var(--brand-brown); opacity: 0.65;
  }

  .bag__roast {
    top: var(--roast-y);
    display: flex; align-items: center; gap: 0.4em; padding: 0 4%;
  }
  .bag__roast::before, .bag__roast::after {
    content: ""; flex: 1; height: 0.45em;
    border-top: 1px solid var(--ink); border-bottom: 1px solid var(--ink);
  }
  .roast__label {
    padding: 0.35em 0.9em; border: 1px solid var(--ink);
    outline: 1px solid var(--ink); outline-offset: 2px;
    background: var(--label-bg, rgba(255,255,255,0.85));
    font-family: "Cinzel", serif; font-weight: 700; font-size: 0.9em; letter-spacing: 0.08em;
    color: var(--label-ink, var(--brand-brown)); white-space: nowrap;
  }

  .bag__product { top: var(--product-y); line-height: 1.05; }
  .product__pct { font-family: "Roboto Slab", serif; font-weight: 700; font-size: 0.75em; }
  .product__name { font-family: "Rye", serif; font-size: 1.9em; letter-spacing: 0.04em; }
  .product__kind {
    display: flex; align-items: center; justify-content: center; gap: 0.5em;
    font-family: "Rye", serif; font-size: 0.8em; letter-spacing: 0.15em;
  }
  .product__kind::before, .product__kind::after { content: ""; width: 2.2em; border-top: 1px solid var(--ink); }
  .product__form {
    margin-top: 0.2em; font-family: "Roboto Slab", serif; font-weight: 700; font-size: 1em;
    letter-spacing: 0.12em; color: var(--form-ink, var(--brand-brown));
  }
  .product__origin {
    margin: 0.5em auto 0; width: 62%;
    font-family: "Lora", serif; font-style: italic; font-size: 0.45em; line-height: 1.3;
    color: var(--origin-ink, var(--brand-brown));
  }
  .product__weight {
    margin-top: 0.6em; font-family: "Roboto Slab", serif; font-weight: 700; font-size: 0.6em;
    color: var(--form-ink, var(--brand-brown));
  }

  .bag--light-ground {
    left: 30px; top: 362px; width: 162px; height: 390px; font-size: 10px;
    --top: var(--light-top); --pattern: var(--light-pattern); --bottom: var(--light-bottom);
    --ink: var(--light-ink); --scene: var(--light-scene);
    --split: 61%; --tag-y: 8%; --logo-y: 27%; --roast-y: 63%; --product-y: 70%; --scene-h: 22%;
  }
  .bag--medium-ground {
    left: 210px; top: 312px; width: 187px; height: 440px; font-size: 11px;
    --top: var(--medium-top); --pattern: var(--medium-pattern); --bottom: var(--medium-bottom);
    --ink: var(--medium-ink); --scene: var(--medium-scene);
    --split: 68%; --tag-y: 18%; --logo-y: 34%; --roast-y: 68%; --product-y: 74%; --scene-h: 22%;
  }
  .bag--medium-beans {
    left: 428px; top: 262px; width: 324px; height: 488px; font-size: 17px;
    --top: var(--medium-top); --pattern: var(--medium-pattern); --bottom: var(--medium-bottom);
    --ink: var(--medium-ink); --scene: var(--medium-scene);
    --split: 55%; --logo-y: 18%; --tag-y: 47%; --roast-y: 54%; --product-y: 62%; --scene-h: 34%;
  }
  .bag--dark-beans {
    left: 768px; top: 178px; width: 412px; height: 564px; font-size: 20px;
    --top: var(--dark-top); --pattern: var(--dark-pattern); --bottom: var(--dark-bottom);
    --ink: var(--dark-ink); --scene: var(--dark-scene);
    --split: 57%; --logo-y: 15%; --tag-y: 44%; --roast-y: 52%; --product-y: 62%; --scene-h: 34%;
    --label-bg: var(--dark-bottom); --label-ink: var(--dark-label);
    --form-ink: var(--dark-label); --origin-ink: #b9aea4;
  }
</style>
</head>
<body>
<main class="range">

  <section class="bag bag--light-ground" aria-label="Light roast ground coffee, 250 g">
    <div class="bag__pattern" role="img" aria-label="Faint engraved floral ornament pattern"></div>
    <div class="bag__seal"></div>
    <div class="bag__scene" role="img" aria-label="Line illustration of Mount Elgon, sun rays and coffee branches"></div>
    <div class="bag__tagline">Specialty<br>Arabica<br>Coffee</div>
    <div class="bag__brand"><span class="brand__disc"></span><span class="brand__name">Nobrelia</span></div>
    <div class="bag__roast"><span class="roast__label">LIGHT ROAST</span></div>
    <div class="bag__product">
      <div class="product__pct">100%</div>
      <div class="product__name">TURKISH</div>
      <div class="product__kind">COFFEE</div>
      <div class="product__form">GROUND</div>
      <p class="product__origin">Grown at slopes of Mountain Elgon with rich volcanic soils located in Eastern region of Uganda.</p>
      <div class="product__weight">250 g</div>
    </div>
  </section>

  <section class="bag bag--medium-ground" aria-label="Medium roast ground coffee, 250 g">
    <div class="bag__pattern" role="img" aria-label="Faint engraved floral ornament pattern"></div>
    <div class="bag__seal"></div>
    <div class="bag__scene" role="img" aria-label="Line illustration of Mount Elgon, sun rays and coffee branches"></div>
    <div class="bag__tagline">Specialty<br>Arabica<br>Coffee</div>
    <div class="bag__brand"><span class="brand__disc"></span><span class="brand__name">Nobrelia</span></div>
    <div class="bag__roast"><span class="roast__label">MEDIUM ROAST</span></div>
    <div class="bag__product">
      <div class="product__pct">100%</div>
      <div class="product__name">TURKISH</div>
      <div class="product__kind">COFFEE</div>
      <div class="product__form">GROUND</div>
      <p class="product__origin">Grown at slopes of Mountain Elgon with rich volcanic soils located in Eastern region of Uganda.</p>
      <div class="product__weight">250 g</div>
    </div>
  </section>

  <section class="bag bag--medium-beans" aria-label="Medium roast coffee beans, 250 g">
    <div class="bag__pattern" role="img" aria-label="Faint engraved floral ornament pattern"></div>
    <div class="bag__seal"></div>
    <div class="bag__scene" role="img" aria-label="Line illustration of Mount Elgon, sun rays and coffee branches"></div>
    <div class="bag__brand"><span class="brand__disc"></span><span class="brand__name">Nobrelia</span></div>
    <div class="bag__tagline">Specialty<br>Arabica<br>Coffee</div>
    <div class="bag__roast"><span class="roast__label">MEDIUM ROAST</span></div>
    <div class="bag__product">
      <div class="product__pct">100%</div>
      <div class="product__name">TURKISH</div>
      <div class="product__kind">COFFEE</div>
      <div class="product__form">BEANS</div>
      <p class="product__origin">Grown at slopes of Mountain Elgon with rich volcanic soils located in Eastern region of Uganda.</p>
      <div class="product__weight">250 g</div>
    </div>
  </section>

  <section class="bag bag--dark-beans" aria-label="Dark roast coffee beans, 1000 g">
    <div class="bag__pattern" role="img" aria-label="Faint engraved floral ornament pattern"></div>
    <div class="bag__seal"></div>
    <div class="bag__scene" role="img" aria-label="Line illustration of Mount Elgon, sun rays and coffee branches"></div>
    <div class="bag__brand"><span class="brand__disc"></span><span class="brand__name">Nobrelia</span></div>
    <div class="bag__tagline">Specialty<br>Arabica<br>Coffee</div>
    <div class="bag__roast"><span class="roast__label">DARK ROAST</span></div>
    <div class="bag__product">
      <div class="product__pct">100%</div>
      <div class="product__name">TURKISH</div>
      <div class="product__kind">COFFEE</div>
      <div class="product__form">BEANS</div>
      <p class="product__origin">Grown at slopes of Mountain Elgon with rich volcanic soils located in Eastern region of Uganda.</p>
      <div class="product__weight">1000 g</div>
    </div>
  </section>

</main>
</body>
</html>
```